The name of the company is Dorvane Holdings, LLC. I would like a business card with a logo.

On the top left, I would like a logo design of a crown and I would like Dorvane over the top of the crown while Investments on the bottom. Please see attached files as an example of crown and positioning of Dorvane Holdings. Then I would like the letters DH in the middle(see picture).

Colors

Designer to choose colors to be used in the design.

```html
<!DOCTYPE html>
<html lang="en">
<head>
<meta charset="utf-8">
<title>Dorvane Holdings – Business Card</title>
<link rel="stylesheet" href="https://fonts.googleapis.com/css2?family=Cinzel:wght@400;500&family=Lato:wght@400&display=swap">
<style>
  :root {
    --backdrop: #2b2b29;
    --card: #111112;
    --card-edge: #1c1c1d;
    --ink: #e9e9e9;
    --ink-soft: #cfcfcf;
    --ink-faint: #3a3a3c;
  }
  * { box-sizing: border-box; margin: 0; padding: 0; }
  html, body {
    width: 1200px; height: 824px; overflow: hidden;
    background: var(--backdrop);
  }
  .canvas { position: relative; width: 1200px; height: 824px; }

  .card {
    position: absolute;
    width: 525px; height: 300px;
    background: var(--card);
    border: 1px solid var(--card-edge);
    border-radius: 3px;
    overflow: hidden;
  }
  .card--front { left: 50px; top: 50px; }
  .card--back  { left: 620px; top: 300px; }

  .wordmark {
    font-family: "Cinzel", serif;
    font-weight: 400;
    letter-spacing: 0.08em;
    text-align: center;
    white-space: nowrap;
    display: flex; flex-direction: column; align-items: center; gap: 10px;
  }
  .wordmark__dot {
    width: 10px; height: 10px; border-radius: 50%;
  }

  .card--front .wordmark {
    position: absolute; left: 0; right: 0; top: 112px;
    color: var(--ink-faint); font-size: 40px;
  }
  .card--front .wordmark__dot { background: var(--ink-faint); }

  .card--back .wordmark {
    position: absolute; left: 28px; top: 36px; align-items: flex-start;
    color: var(--ink-soft); font-size: 20px; gap: 8px;
  }
  .card--back .wordmark__dot { background: var(--ink-soft); width: 8px; height: 8px; }

  .contact {
    position: absolute; left: 28px; top: 150px;
    list-style: none;
    font-family: "Lato", sans-serif; font-size: 13px; line-height: 21px;
    color: var(--ink-soft);
  }
  .contact li { display: flex; align-items: center; gap: 8px; white-space: nowrap; }
  .contact .indent { padding-left: 18px; }
  .contact svg { width: 10px; height: 10px; fill: var(--ink-soft); flex: none; }

  .holder {
    position: absolute; right: 30px; top: 96px; text-align: right;
    font-family: "Cinzel", serif; font-weight: 500; color: var(--ink);
    font-size: 17px; line-height: 26px; letter-spacing: 0.03em;
    white-space: nowrap;
  }

  .lockup {
    position: absolute; left: 50px; top: 660px;
    color: #ffffff; font-size: 42px;
  }
  .lockup .wordmark__dot { background: #ffffff; }
</style>
</head>
<body>
<main class="canvas">

  <section class="card card--front" aria-label="Card front">
    <div class="wordmark">
      <span class="wordmark__dot"></span>
      <span>Dorvane Holdings</span>
    </div>
  </section>

  <section class="card card--back" aria-label="Card back">
    <div class="wordmark">
      <span class="wordmark__dot"></span>
      <span>Dorvane Holdings</span>
    </div>

    <div class="holder">
      <p>Teo Marlow Dorvane, MBA</p>
      <p>Founder/CEO</p>
    </div>

    <ul class="contact">
      <li>
        <svg viewBox="0 0 10 10" aria-hidden="true"><path d="M5 0a3.5 3.5 0 0 0-3.5 3.5C1.5 6 5 10 5 10s3.5-4 3.5-6.5A3.5 3.5 0 0 0 5 0zm0 5a1.5 1.5 0 1 1 0-3 1.5 1.5 0 0 1 0 3z"/></svg>
        Dorvane Holdings, LLC
      </li>
      <li class="indent">412 Linden Crest Drive, Suite 300</li>
      <li class="indent">Maple Hollow, CA 90000</li>
      <li>
        <svg viewBox="0 0 10 10" aria-hidden="true"><path d="M2 0l2 2.5-1 1.2c.6 1.3 1.6 2.3 2.8 2.8l1.2-1L10 8l-1.5 2C4 10 0 6 0 1.5z"/></svg>
        (555) 014-2290
      </li>
      <li>
        <svg viewBox="0 0 10 10" aria-hidden="true"><path d="M0 2h10v6H0zM0.8 2.6 5 5.6l4.2-3V2.8L5 5 0.8 2.8z"/></svg>
        t.dorvane.holdings@example.com
      </li>
    </ul>
  </section>

  <div class="wordmark lockup">
    <span class="wordmark__dot"></span>
    <span>Dorvane Holdings</span>
  </div>

</main>
</body>
</html>
```